Bright Path Flyer Design for Virtual Online Clinic. -5.5 x 8.5 inches (half sheet)

We need a clean, modern flyer design for Bright Path, a new virtual walk-in clinic based in British Columbia. The flyer will be used in libraries, pharmacies, and community centers to help residents easily access primary care through their Bright Path NFC access card.
The flyer will ask a question : NEED A DOCTOR? This should be large and attention grabbing.
The design should clearly feature a Bright Path card image (the access card) as the centerpiece and visually show how patients can use it to book appointments. The tone should feel trustworthy, healthcare-oriented, and community-friendly — clean fonts, clear spacing, and strong readability from a distance.

Side One: This card has the NFC Access Card.
NEED A DOCTOR? (Large Font, Attention Grabbing)
How to Book an Appointment using your Bright Path Card
Step 1: Tap Your Card on Your Phone
Hold your card near the back of your phone.
It will activate automatically — no app needed.
The Bright Path scheduler will open.
Step 2: Schedule Your Appointment
Select your clinical concern.
Choose your time window.
Register (only once).
Confirm your appointment.
Step 3: Relax, we’ll take care of the rest
A doctor will call during your scheduled time.
Once booked, you’ll be able to call our office.
No emails, no texts — just a real person.
It’s that simple.
Side Two:
About Bright Path
Created by Dr. Marcus Ferrigan
Bright Path was founded to make healthcare simple and convenient. Prescription renewals. Common infections. Medical notes. And so much more.
Our doctors can address 120+ health concerns virtually — providing quality care without the waiting room. No waiting rooms. Just real doctors providing real care.
Why Patients Choose Bright Path
Easy access – book and be seen from anywhere in BC.
Effortless booking – tap your Bright Path Card to begin.
Trusted physicians – every visit is with a licensed BC family doctor.
How It Works
Book your visit — choose a time window that fits your day.
Join the queue — you’ll be called when it’s your turn.
Speak directly with your doctor — simple, secure, and stress-free.
Convenient Care for Common Concerns

Additional Details.
Please find the domain to be launched soon. I've attached the NFC card file for review, it is 85.5 mm x 54 mm. The card will be glued to the flyer.
I've attached examples of flyers but they are not the look I am seeking and I am looking for creative solutions.
Thank you!
http://brightpath-example.test/

Adult Patients in British Columbia

Healthcare

• Looking for clean lines, uniform appearance, and high legibility i.e poppins

0054AA
0677BA
7BADD7
CADEEF
E8F1F8

• Need A Doctor?
• Elegant style, not too busy, clear layout.
• Clutter, look cheap - review examples.

```html
<!DOCTYPE html>
<html lang="en">
<head>
<meta charset="utf-8">
<title>Bright Path – Flyer</title>
<link rel="stylesheet" href="https://fonts.googleapis.com/css2?family=Poppins:wght@400;500;600;700&family=Rubik:wght@500;600;700&family=Tinos:wght@400;700&display=swap">
<style>
:root{
  --navy:#0a4a86;
  --blue:#0054AA;
  --teal:#0677BA;
  --aqua:#1aa3cf;
  --sky:#7BADD7;
  --mist:#CADEEF;
  --ice:#E8F1F8;
  --panel:#f1f3f6;
  --col-a:#e6eaef;
  --col-b:#dde2e8;
  --col-c:#edf0f3;
  --stage:#e9ebee;
  --white:#ffffff;
}
*{box-sizing:border-box;margin:0;padding:0}
html,body{width:1200px;height:842px;overflow:hidden}
body{background:var(--stage);font-family:"Poppins",Arial,sans-serif;color:var(--navy);position:relative}
.abs{position:absolute}

/* ---------- shared ---------- */
.sheet{position:absolute;top:25px;width:554px;height:782px;background:var(--white);overflow:hidden;box-shadow:0 4px 14px rgba(0,0,0,.18)}
.sheet--front{left:40px;background:var(--panel)}
.sheet--back{left:610px}
.brand{font-family:"Poppins",Arial,sans-serif;font-weight:500;color:var(--blue);font-size:22px;letter-spacing:.2px}
.url{font-family:"Rubik",Arial,sans-serif;font-weight:500;font-size:11px;color:var(--navy)}
.dots{display:flex;gap:5px}
.dots i{display:block;width:8px;height:8px;border-radius:50%;background:var(--aqua)}
.dots--grey i{background:#c9ccd1;width:11px;height:11px}
.pill{background:linear-gradient(90deg,var(--navy),var(--teal) 60%,var(--aqua));color:var(--white);font-family:"Rubik",Arial,sans-serif;font-weight:700;border-radius:0 8px 8px 0}

/* ---------- front ---------- */
.front-logo{left:32px;top:34px}
.headline{left:32px;top:74px;font-family:"Rubik",Arial,sans-serif;font-weight:700;font-size:60px;line-height:58px;color:var(--navy);letter-spacing:.5px}
.subhead{left:30px;top:198px;font-family:"Tinos",Georgia,serif;font-size:33px;line-height:34px;color:var(--navy)}
.portrait{left:320px;top:0;width:234px;height:380px;background:linear-gradient(180deg,#eef0f2,#dfe2e6 60%,#cfd4da)}
.front-dots-top{left:492px;top:20px}
.front-dots-mid{left:16px;top:366px}
.band{left:0;top:380px;width:554px;height:15px;background:var(--aqua)}
.band-end{left:486px;top:380px;width:68px;height:15px;background:var(--navy)}
.cols{left:0;top:395px;width:554px;height:387px;display:flex;gap:3px}
.col{flex:1;position:relative}
.col:nth-child(1){background:var(--col-a)}
.col:nth-child(2){background:var(--col-b)}
.col:nth-child(3){background:var(--col-c)}
.cards{left:58px;top:330px;width:450px;height:200px}
.step{position:absolute;left:29px;top:133px;width:150px}
.step__tag{display:flex;align-items:center;gap:6px}
.step__tag .pill{font-size:14px;padding:1px 8px 0 5px;border-radius:0 4px 4px 0;line-height:19px}
.step__tag .dots i{width:5px;height:5px}
.step__title{margin-top:6px;font-family:"Rubik",Arial,sans-serif;font-weight:600;font-size:11.5px;line-height:16px;text-transform:uppercase;color:var(--navy)}
.step__list{list-style:none;margin-top:12px}
.step__list li{font-size:10.5px;line-height:13.5px;margin-bottom:7.5px;color:#12365e}
.col:nth-child(2) .step{left:14px}
.col:nth-child(3) .step{left:20px}
.front-url{left:29px;top:759px}
.tagline{left:375px;top:727px;width:179px;height:46px;font-size:17px;display:flex;align-items:center;justify-content:center;border-radius:6px 0 0 0}
.front-dots-bottom{left:337px;top:766px}
.front-dots-bottom i{width:6px;height:6px}

/* ---------- back ---------- */
.hero{left:0;top:0;width:554px;height:175px;background:linear-gradient(100deg,#8a857e,#b9b4ac 45%,#6f6a63)}
.about{left:0;top:50px;width:220px;height:92px;font-family:"Tinos",Georgia,serif;font-weight:700;font-size:32px;line-height:37px;padding:8px 0 0 24px;border-radius:0 8px 8px 0}
.hero-dots{left:492px;top:156px}
.hero-dots i{background:#e7e7e7}
.band-back{left:0;top:175px;width:554px;height:15px;background:linear-gradient(90deg,var(--aqua),var(--teal) 45%,var(--navy))}
.creator{left:24px;top:204px;font-family:"Tinos",Georgia,serif;color:var(--navy)}
.creator__lead{font-size:29px;line-height:32px}
.creator__name{font-size:35px;line-height:40px;font-weight:700}
.intro{left:24px;top:282px;width:510px;font-size:12.2px;line-height:16px;color:var(--blue)}
.intro p+p{margin-top:12px}
.section-grey{left:0;top:380px;width:554px;height:175px;background:#eef0f3}
.section-pill{left:24px;font-size:17.5px;line-height:24px;padding:6px 10px 6px 8px}
.why{top:400px}
.how{top:575px}
.list{left:24px;list-style:none;font-size:14.6px;line-height:21.3px;color:var(--blue)}
.why-list{top:478px}
.how-list{top:623px}
.back-logo{left:372px;top:732px}
.back-url{left:431px;top:759px}
</style>
</head>
<body>

<!-- FRONT -->
<section class="sheet sheet--front" aria-label="Front: how to book">
  <div class="abs portrait" role="img" aria-label="Photo of a smiling doctor in a white coat holding a tablet"></div>
  <div class="abs dots dots--grey front-dots-top"><i></i><i></i><i></i></div>

  <div class="abs brand front-logo">Bright Path</div>
  <h1 class="abs headline">NEED A<br>DOCTOR?</h1>
  <p class="abs subhead">How to Book<br>an Appointment<br>using your<br>Bright Path Card</p>
  <div class="abs dots front-dots-mid"><i></i><i></i><i></i></div>

  <div class="abs band"></div>
  <div class="abs band-end"></div>

  <div class="abs cols">
    <div class="col">
      <div class="step">
        <div class="step__tag"><span class="pill">STEP 1</span><span class="dots"><i></i><i></i><i></i></span></div>
        <h2 class="step__title">Tap your card<br>on your phone</h2>
        <ul class="step__list">
          <li>Hold your card near the back of your phone.</li>
          <li>It will activate automatically — no app needed.</li>
          <li>The Bright Path scheduler will open.</li>
        </ul>
      </div>
    </div>
    <div class="col">
      <div class="step">
        <div class="step__tag"><span class="pill">STEP 2</span><span class="dots"><i></i><i></i><i></i></span></div>
        <h2 class="step__title">Schedule your<br>appointment</h2>
        <ul class="step__list">
          <li>Select your clinical concern.</li>
          <li>Choose your time window.</li>
          <li>Register (only once).</li>
          <li>Confirm your appointment.</li>
        </ul>
      </div>
    </div>
    <div class="col">
      <div class="step">
        <div class="step__tag"><span class="pill">STEP 3</span><span class="dots"><i></i><i></i><i></i></span></div>
        <h2 class="step__title">Relax, we’ll take<br>care of the rest</h2>
        <ul class="step__list">
          <li>A doctor will call during your scheduled time.</li>
          <li>Once booked, you’ll be able to call our office.</li>
          <li>No emails, no texts — just a real person.</li>
        </ul>
      </div>
    </div>
  </div>

  <svg class="abs cards" viewBox="0 0 450 200" role="img" aria-label="Bright Path NFC access card, front and back">
    <rect x="10" y="40" width="230" height="135" rx="10" fill="#1f3f92" transform="rotate(-8 125 107)"/>
    <rect x="205" y="25" width="230" height="135" rx="10" fill="#f4f6fa" stroke="#d5dbe4" transform="rotate(-8 320 92)"/>
    <path d="M205 40 L300 27 L290 172 L222 181 Z" fill="#1f3f92" transform="rotate(-8 320 92)" opacity="0"/>
  </svg>

  <div class="abs url front-url">www.brightpath-example.test</div>
  <div class="abs pill tagline">It’s that Simple.</div>
  <div class="abs dots front-dots-bottom"><i></i><i></i><i></i></div>
</section>

<!-- BACK -->
<section class="sheet sheet--back" aria-label="Back: about the clinic">
  <div class="abs hero" role="img" aria-label="Photo of a stethoscope on a wooden table"></div>
  <h1 class="abs pill about">About<br>Bright Path</h1>
  <div class="abs dots dots--grey hero-dots"><i></i><i></i><i></i></div>
  <div class="abs band-back"></div>

  <div class="abs creator">
    <div class="creator__lead">Created by</div>
    <div class="creator__name">Dr. Marcus Ferrigan</div>
  </div>
  <div class="abs intro">
    <p>Bright Path was founded to make healthcare simple and convenient.<br>Prescription renewals. Common infections. Medical notes. And so much more.</p>
    <p>Our doctors can address 120+ health concerns virtually — providing quality care<br>without the waiting room. No waiting rooms. Just real doctors providing real care.</p>
  </div>

  <div class="abs section-grey"></div>
  <h2 class="abs pill section-pill why">WHY PATIENTS CHOOSE<br>BRIGHT PATH &nbsp;●●●</h2>
  <ul class="abs list why-list">
    <li>Easy access – book and be seen from anywhere in BC.</li>
    <li>Effortless booking – tap your Bright Path Card to begin.</li>
    <li>Trusted physicians – every visit is with a licensed BC family doctor.</li>
  </ul>

  <h2 class="abs pill section-pill how">HOW IT WORKS &nbsp;●●●</h2>
  <ul class="abs list how-list">
    <li>Book your visit — choose a time window that fits your day.</li>
    <li>Join the queue — you’ll be called when it’s your turn.</li>
    <li>Speak directly with your doctor — simple, secure, and stress-free.</li>
    <li>Convenient Care for Common Concerns</li>
  </ul>

  <div class="abs brand back-logo">Bright Path</div>
  <div class="abs url back-url">www.brightpath-example.test</div>
</section>

</body>
</html>
```